Home Page Re-Design for Job Interview Training Website

Hi all,

I require a refresh of my home page here www.parlowquest.com

I will keep the logo and branding colours and video - however the video can be re-sized and re-design as required to fit with the new site.

All other aspects are open to re-design however while I want it to look new and updated visitors must be able to recognise that it is the same website.

I have a wireframe/mock up however I will require you to use your excellent design skills to make it look great. This is just a rough guide so be creative with where you place blocks, content and images - design does not have to follow this wireframe strictly. So long as all content can be included in a clean minimalist manner.

Re-design in summary:
1. Clean, easy to read
2. Professional
3. Message of Trust and Success
4. Use success stories and in the press stories to convey trust
5. Re-design menu and calls to action
6. Re-design buttons

I need blocks added as follows:
1. For Universities
2. For Employers
3. For Specialist Interviews
4. In the Press
5. Quote from successful client/success story
6. Sign up to newsletter

Text to be added to the page.
1. Show text in full - not click to read as at present
2. Additional block called Interview Answer Test - see wireframe

Sites I like:
http://www.trelvanpath.org/course
http://brondix.com/

NOTE: While wireframe includes images from the above sites obviously you will need to re-design to fit my site. The wireframe is just to give you a broad idea of what I have in mind but feel free to be as creative as possible.

Winning design will be clean, fresh, gives a message of success and trust, modern and in line with my branding. I prefer minimal, clean, web 2.0 style designs, limited colours.

Also the winner will be someone whose design makes me excited and gives me something that I haven't thought of myself.

UPDATE: main body text must be on a white background, not dark or coloured

Ask any questions
Thanks

Target Market(s)

People looking for a job with a job interview imminent

Industry/Entity Type

Training

Requirements
Must have
• Clean fresh design
Should not have
• No Gaudy colours or use of standard templates

```html
<!DOCTYPE html>
<html lang="en">
<head>
<meta charset="utf-8">
<title>InterviewCrest – Online Interview Skills Training</title>
<link rel="stylesheet" href="https://fonts.googleapis.com/css2?family=Arimo:wght@400;700&family=Arvo:wght@400;700&display=swap">
<style>
:root{
  --backdrop:#2a2623;
  --page:#ffffff;
  --hero-bg:#e8edf3;
  --band-bg:#f2f4f7;
  --header:#7d95ba;
  --header-top:#4e6589;
  --login:#3c4d69;
  --footer:#43597e;
  --navy:#1d4e7c;
  --heading:#1f5a8c;
  --text:#4a4a4a;
  --muted:#7a7a7a;
  --sky:#2f93d2;
  --sky-light:#63b1d8;
  --sky-dark:#1d78b8;
  --orange:#f7801f;
  --orange-light:#fca34a;
  --green:#6fae2b;
  --green-light:#8ccb3c;
  --green-panel:#e3efd3;
  --white:#ffffff;
  --rule:#d8dee6;
}
*{box-sizing:border-box;margin:0;padding:0}
html,body{width:1200px;height:900px;overflow:hidden}
body{background:var(--backdrop);font-family:"Arimo",Arial,sans-serif;color:var(--text);position:relative}
.site{position:absolute;left:315px;top:22px;width:570px;height:856px;background:var(--page);overflow:hidden}
.abs{position:absolute}

/* header */
.site-header{left:0;top:0;width:570px;height:30px;background:var(--header);border-top:3px solid var(--header-top)}
.brand{left:100px;top:6px;display:flex;align-items:center;gap:4px}
.brand-dot{width:11px;height:11px;border-radius:50%;background:var(--white)}
.brand-name{font:700 10px "Arimo",sans-serif;color:var(--white);line-height:1}
.main-nav{left:228px;top:11px;display:flex;gap:5px;font-size:5.2px;color:var(--white)}
.main-nav .buy{font-weight:700}
.login{left:442px;top:0;width:29px;height:27px;background:var(--login);color:var(--white);font-size:4.8px;text-align:center;padding-top:5px}
.login svg{display:block;margin:0 auto 2px}

/* hero */
.hero{left:0;top:30px;width:570px;height:198px;background:var(--hero-bg);border-bottom:1px solid var(--rule)}
.video{left:99px;top:7px;width:252px;height:184px}
.video-photo{width:100%;height:100%;background:linear-gradient(135deg,#d9c3a6 0%,#b99a78 40%,#8d8c91 70%,#5d5f66 100%)}
.video-bar{left:0;bottom:0;width:252px;height:26px;background:rgba(0,0,0,.35)}
.play{left:4px;top:4px;width:24px;height:18px;background:#2b2b2b;border:1px solid #6a6a6a}
.track{left:34px;top:11px;width:178px;height:3px;background:#8b8b8b}
.track span{display:block;width:68px;height:3px;background:var(--white)}
.hd{left:225px;top:8px;font:700 6px "Arimo",sans-serif;color:var(--sky-light)}

.start{left:356px;top:7px;width:114px;height:98px;background:var(--sky-light)}
.start-title{height:24px;background:var(--sky);color:var(--white);font:400 11px "Arvo",serif;text-align:center;line-height:24px}
.start-copy{font-size:5.4px;color:var(--white);text-align:center;line-height:1.35;padding:6px 10px 0}
.start-copy b{display:block;margin-top:4px}
.btn{display:block;text-align:center;color:var(--white);font:400 7.5px "Arvo",serif;letter-spacing:.3px;background:linear-gradient(var(--orange-light),var(--orange));border-radius:2px}
.start .btn{position:absolute;left:9px;top:72px;width:108px;height:24px;line-height:24px;color:#5a2e05}

.side-box{left:356px;width:114px;height:40px;background:var(--sky-light)}
.side-box h3{height:12px;background:var(--sky);color:var(--white);font:400 5.8px "Arvo",serif;text-align:center;line-height:12px}
.versions{display:flex;justify-content:center;gap:4px;align-items:center;padding-top:8px;font-size:4.5px;color:var(--white)}
.flag{width:18px;height:12px;display:inline-block}
.partners{display:flex;justify-content:center;gap:6px;padding-top:7px}
.badge{width:42px;height:14px;background:var(--white);border-radius:1px}

/* content */
.content{left:0;top:228px;width:570px;height:298px;background:var(--white)}
.intro{left:103px;top:10px;width:222px}
.intro h2{font:400 7.2px "Arimo",sans-serif;color:var(--heading);margin-bottom:7px;line-height:1.3}
.intro p{font-size:4.3px;line-height:1.45;color:var(--text);margin-bottom:5px}
.intro h2.gap{margin-top:13px}

.audience{left:356px;width:114px;height:80px;background:var(--green-panel)}
.audience h3{height:21px;background:linear-gradient(var(--green-light),var(--green));color:var(--white);font:700 5.2px "Arimo",sans-serif;padding:4px 9px;line-height:1.3}
.audience p{font-size:4.4px;line-height:1.35;padding:5px 9px 0;color:var(--text)}
.audience a{display:block;font-size:5.2px;padding:5px 7px 0;color:var(--navy);text-decoration:underline}

/* test band */
.test{left:0;top:526px;width:570px;height:132px;background:var(--band-bg);border-top:1px solid var(--rule)}
.test h2{left:103px;top:12px;font:400 7.2px "Arimo",sans-serif;color:var(--heading)}
.test .btn{position:absolute;left:368px;top:8px;width:85px;height:19px;line-height:19px}
.test p{left:103px;top:34px;width:352px;font-size:4.3px;line-height:1.4}
.q-card{top:67px;width:115px;height:53px;background:linear-gradient(var(--sky),var(--sky-dark));border-radius:2px;color:var(--white)}
.q-card h4{font:400 7.5px "Arvo",serif;padding:4px 9px 2px}
.q-card p{position:static;width:78px;font-size:4.3px;line-height:1.3;padding:0 9px;color:#e9f4fb}
.q-card .arrow{position:absolute;right:2px;top:16px}

/* press */
.press{left:0;top:658px;width:570px;height:42px;background:var(--white);border-top:1px solid var(--rule);border-bottom:1px solid var(--rule)}
.press h2{left:103px;top:6px;font:400 5px "Arimo",sans-serif;color:var(--text)}
.press-logos{left:104px;top:22px;display:flex;gap:7px}
.press-logos span{height:10px;background:#dfe4ea;border-radius:1px}

/* bottom */
.lower{left:0;top:700px;width:570px;height:128px;background:var(--band-bg)}
.quote{left:103px;top:6px;width:180px;height:117px;background:var(--white);border:1px solid var(--rule)}
.quote h3{left:9px;top:7px;font:400 7px "Arimo",sans-serif;color:var(--heading)}
.quote-rule{left:9px;top:18px;width:162px;border-top:1px dotted #c9c9c9}
.avatar{left:14px;top:27px;width:18px;height:28px;background:linear-gradient(#d9c49a,#b7a17f)}
.quote blockquote{left:9px;top:58px;width:165px;font-size:4.5px;line-height:1.35;color:var(--text)}
.quote cite{left:90px;top:88px;font-size:4.5px;font-style:normal;color:#333}
.quote .pager{left:12px;top:102px;width:155px;display:flex;justify-content:space-between;font-size:4.6px;color:var(--navy)}

.newsletter{left:295px;top:12px;width:165px}
.newsletter h3{font:400 9px "Arvo",serif;color:#333;margin-bottom:6px}
.newsletter p{font-size:4.5px;line-height:1.35;color:var(--text)}
.email{left:295px;top:62px;width:160px;height:14px;background:var(--white);border:1px solid #cfd5dc;font-size:4.8px;color:#aaa;padding:4px 5px}
.lower .btn{position:absolute;left:369px;top:82px;width:85px;height:19px;line-height:19px}

/* footer */
.site-footer{left:0;top:828px;width:570px;height:28px;background:var(--footer);color:#dce4ef;font-size:4.4px}
.footer-links{left:100px;top:7px;line-height:1.5}
.copyright{left:409px;top:10px}
</style>
</head>
<body>
<div class="site">

  <header class="site-header abs">
    <div class="brand abs"><span class="brand-dot"></span><span class="brand-name">InterviewCrest</span></div>
    <nav class="main-nav abs">
      <span>Home</span><span>About InterviewCrest</span><span>Success Story</span><span>Partners</span><span>FAQ</span><span>Contact Us</span><span class="buy">BUY NOW!</span>
    </nav>
    <div class="login abs">
      <svg width="7" height="9" viewBox="0 0 7 9"><path d="M1.5 4V2.6a2 2 0 0 1 4 0V4" fill="none" stroke="#fff" stroke-width="1"/><rect x="0.5" y="4" width="6" height="4.5" fill="#fff"/></svg>
      Login
    </div>
  </header>

  <section class="hero abs">
    <div class="video abs">
      <div class="video-photo" role="img" aria-label="Video still: a candidate writing notes with a pen at a table during interview practice"></div>
      <div class="video-bar abs">
        <div class="play abs"><svg width="22" height="16" viewBox="0 0 22 16"><path d="M8 4l7 4-7 4z" fill="#fff"/></svg></div>
        <div class="track abs"><span></span></div>
        <div class="hd abs">HD</div>
      </div>
    </div>

    <div class="start abs">
      <div class="start-title">Start Today!</div>
      <div class="start-copy">Get started with<br>InterviewCrest today and<br>succeed in your next interview<b>GET INSTANT ACCESS NOW<br>100% GUARANTEED</b></div>
      <a class="btn">LEARN MORE</a>
    </div>

    <div class="side-box abs" style="top:109px">
      <h3>Version available for:</h3>
      <div class="versions">
        <span>UK/NZ</span>
        <svg class="flag" viewBox="0 0 18 12" aria-label="UK version"><rect width="18" height="12" fill="#24407e"/><path d="M0 0L18 12M18 0L0 12" stroke="#fff" stroke-width="2.4"/><path d="M0 0L18 12M18 0L0 12" stroke="#c8202f" stroke-width="0.9"/><path d="M9 0V12M0 6H18" stroke="#fff" stroke-width="3.6"/><path d="M9 0V12M0 6H18" stroke="#c8202f" stroke-width="2"/></svg>
        <span>US</span>
        <svg class="flag" viewBox="0 0 18 12" aria-label="US version"><rect width="18" height="12" fill="#fff"/><path d="M0 1H18M0 3.6H18M0 6.2H18M0 8.8H18M0 11.3H18" stroke="#c8202f" stroke-width="1.1"/><rect width="8" height="6.5" fill="#2b3f7a"/></svg>
        <span>AUS</span>
        <svg class="flag" viewBox="0 0 18 12" aria-label="Australian version"><rect width="18" height="12" fill="#1f3a7e"/><path d="M4 0V6M0 3H8" stroke="#fff" stroke-width="1.6"/><path d="M4 0V6M0 3H8" stroke="#c8202f" stroke-width="0.7"/><circle cx="4" cy="9" r="1" fill="#fff"/><circle cx="13" cy="3" r=".7" fill="#fff"/><circle cx="15" cy="6" r=".7" fill="#fff"/><circle cx="13" cy="9.5" r=".7" fill="#fff"/></svg>
      </div>
    </div>

    <div class="side-box abs" style="top:152px">
      <h3>In Partnership With:</h3>
      <div class="partners"><span class="badge"></span><span class="badge"></span></div>
    </div>
  </section>

  <main class="content abs">
    <article class="intro abs">
      <h2>Welcome to InterviewCrest™ Online Interview Skills Training</h2>
      <p>Lorem Ipsum is simply dummy text of the printing and typesetting industry. Lorem Ipsum has been the industry's standard dummy text ever since the 1500s, when an unknown printer took a galley of type and scrambled it to make a type specimen book. It has survived not only five centuries, but also the leap into electronic typesetting, remaining essentially unchanged. It was popularised in the 1960s with the release of Typeset sheets containing Lorem Ipsum passages, and more recently with desktop publishing software like Quill PageSetter including versions of Lorem Ipsum.</p>
      <p>It is a long established fact that a reader will be distracted by the readable content of a page when looking at its layout. The point of using Lorem Ipsum is that it has a more-or-less normal distribution of letters, as opposed to using 'Content here, content here', making it look like readable English. Many desktop publishing packages and web page editors now use Lorem Ipsum as their default model text, and a search for 'lorem ipsum' will uncover many web sites still in their infancy. Various versions have evolved over the years, sometimes by accident, sometimes on purpose (injected humour and the like).</p>
      <p>There are many variations of passages of Lorem Ipsum available, but the majority have suffered alteration in some form, by injected humour, or randomised words which don't look even slightly believable. If you are going to use a passage of Lorem Ipsum, you need to be sure there isn't anything embarrassing hidden in the middle of text. All the Lorem Ipsum generators on the Internet tend to repeat predefined chunks as necessary, making this the first true generator on the Internet.</p>
      <h2 class="gap">Online Interview Skills Training<br>With Interview Questions and Expert Answers</h2>
      <p>We are in the midst of one of the deepest recessions for many years and as a consequence there are many applicants chasing fewer jobs. To win that elusive job offer, excellent interview skills are essential and with InterviewCrest, you will quickly and easily learn how to excel in any job interview and secure the job. It gives you everything you need for a great interview performance including accurate interview questions and expert model interview answers.</p>
      <h2 class="gap">Dramatically Boost Your Chances of Interview Success</h2>
      <p>For the majority of candidates a job interview can be stressful and nerve wracking. Most worry about the interview questions that can arise and many are unsure which interview answers they should give. With InterviewCrest you will discover the interview questions most likely to arise in your actual interview and with an expert interview answer to each questions you can be confident of knowing just what to say to get the job. InterviewCrest combines a unique set of features which have been shown to increase your chances of winning the job offer by 92%.</p>
    </article>

    <aside class="audience abs" style="top:11px">
      <h3>InterviewCrest<br>For Employers &amp; Recruiters</h3>
      <p>InterviewCrest™ will give your staff and candidates the confidence and skills to excel in any job interview. Whether it's a Competency Based or Panel Interview, internal or external interview</p>
      <a>Click here to read more »</a>
    </aside>
    <aside class="audience abs" style="top:92px">
      <h3>InterviewCrest<br>For Universities</h3>
      <p>InterviewCrest™ will give your staff and candidates the confidence and skills to excel in any job interview. Whether it's a Competency Based or Panel Interview, internal or external interview</p>
      <a>Click here to read more »</a>
    </aside>
    <aside class="audience abs" style="top:172px">
      <h3>InterviewCrest<br>For Specialist Interview</h3>
      <p>InterviewCrest™ will give your staff and candidates the confidence and skills to excel in any job interview. Whether it's a Competency Based or Panel Interview, internal or external interview</p>
      <a>Click here to read more »</a>
    </aside>
  </main>

  <section class="test abs">
    <h2 class="abs">Interview Question Test</h2>
    <a class="btn">LEARN MORE</a>
    <p class="abs">Lorem Ipsum is simply dummy text of the printing and typesetting industry. Lorem Ipsum has been the industry's standard dummy text ever since the 1500s, when an unknown printer took a galley of type and scrambled it to make a type specimen book. It has survived not only five centuries, but also the leap into electronic typesetting, remaining essentially unchanged. It was popularised in the 1960s with the release of Typeset sheets containing Lorem Ipsum passages, and more recently with desktop publishing software like Quill PageSetter including versions of Lorem Ipsum.</p>
    <div class="q-card abs" style="left:102px">
      <h4>01 Interview Question</h4>
      <p>Lorem Ipsum is simply dummy text of the printing and typesetting industry. Lorem Ipsum has been the industry's standard dummy text ever since the 1500s, when an unknown printer.</p>
      <svg class="arrow" width="14" height="18" viewBox="0 0 14 18"><circle cx="9" cy="9" r="9" fill="#e6f3fb"/><path d="M7 5l6 4-6 4z" fill="#2f93d2"/></svg>
    </div>
    <div class="q-card abs" style="left:220px">
      <h4>02 Interview Question</h4>
      <p>Lorem Ipsum is simply dummy text of the printing and typesetting industry. Lorem Ipsum has been the industry's standard dummy text ever since the 1500s, when an unknown printer.</p>
      <svg class="arrow" width="14" height="18" viewBox="0 0 14 18"><circle cx="9" cy="9" r="9" fill="#e6f3fb"/><path d="M7 5l6 4-6 4z" fill="#2f93d2"/></svg>
    </div>
    <div class="q-card abs" style="left:338px">
      <h4>02 Interview Question</h4>
      <p>Lorem Ipsum is simply dummy text of the printing and typesetting industry. Lorem Ipsum has been the industry's standard dummy text ever since the 1500s, when an unknown printer.</p>
      <svg class="arrow" width="14" height="18" viewBox="0 0 14 18"><circle cx="9" cy="9" r="9" fill="#e6f3fb"/><path d="M7 5l6 4-6 4z" fill="#2f93d2"/></svg>
    </div>
  </section>

  <section class="press abs">
    <h2 class="abs">As Recommended by Top Recruiters and in The Press</h2>
    <div class="press-logos abs">
      <span style="width:40px"></span><span style="width:45px"></span><span style="width:52px"></span><span style="width:29px"></span><span style="width:53px"></span><span style="width:31px"></span>
    </div>
  </section>

  <section class="lower abs">
    <div class="quote abs">
      <h3 class="abs">What people are saying</h3>
      <div class="quote-rule abs"></div>
      <div class="avatar abs" role="img" aria-label="Portrait of the quoted customer"></div>
      <blockquote class="abs">"Trelvanpath helped me realise that there were many small steps I could take towards improving my job satisfaction. Gaining greater focus has given me a renewed enthusiasm for my work, giving me the confidence to negotiate a one year sabbatical."</blockquote>
      <cite class="abs">Marla - Administrator, London</cite>
      <div class="pager abs"><span>&lt;&lt; Prev</span><span>Next &gt;&gt;</span></div>
    </div>

    <div class="newsletter abs">
      <h3>Newsletter SIGN UP!</h3>
      <p>On the other hand, we denounce with righteous indignation and dislike men who are so beguiled and demoralized by the charms of pleasure of the moment, so blinded by desire, that they cannot foresee the pain and trouble that are bound to ensue.</p>
    </div>
    <div class="email abs">Your email</div>
    <a class="btn">SIGN UP</a>
  </section>

  <footer class="site-footer abs">
    <div class="footer-links abs">Interview Questions &amp; Answers &nbsp;|&nbsp; Sitemap &nbsp;|&nbsp; Terms &nbsp;|&nbsp; Privacy &nbsp;|&nbsp; Affiliates &nbsp;|&nbsp; Resources<br>Medical Interviews &nbsp;|&nbsp; Nursing Interviews &nbsp;|&nbsp; Competency Based Interviews &nbsp;|&nbsp; Teacher Interviews</div>
    <div class="copyright abs">© 2005 - 2011 Halvern Reed Ltd</div>
  </footer>

</div>
</body>
</html>
```